Flowy subpage design wanted for a modern tax/accounting firm in Switzerland

--- Introduction ---
We are a tax and accounting firm in Switzerland. We provide services for expats living in Switzerland, our service is quite exclusive and modern (digital).

We just relaunched our website www.fiscaverde.ch and are happy with the design, so the desired subpage (more details below) should of course fit in.

--- Main brief ---
Please see Word File attached. The page has to include the whole text (11 chapters). A very intuitive, flowy design on only one subpage (not one page per chapter) is a MUST. Also, it is key that the design is supporting the content of the individual chapters, so it would be advantageous if you'd have a good unterstanding of the text attached.

--- Further information ---
A similar example would be this one: https://www2.brennmark.com/ch/en/pages/tax/articles/living-working-switzerland.html

This one is similar in what concerns the content, but NOT what we are looking for designwise. It is very simple and looks "thrown together", just not aesthetically pleasing in our opinion.

--- Final thoughts ---
- If you blow our minds with your design, we will certainly have future work for you.
- Our clients are between 20-50 years old, well educated, high income / high wealth, English speaking and living in Switzerland.
- CI/CD information:
Fonts
Montserrat regular / medium italic / bold
Colors
White #ffffffff
Darkblue #0a2b46
Darkblue 25% #b5bfc8
Darkblue 50% #8595a4
Greenblue #0d4261

We are looking forward to your designs!
Updates

Thank you very much for the submitted designs and your efforts. Unfortunately, none of the designs meet our expectations so far. Please note the following: - Designs that do not take CI into account will not be looked at more closely. - We have received many simple designs with very simple structure and accordion elements. But more important than the simple structure is an eye-catching design! Make it flowy and beautiful - We don't want pictures of Swiss vehicles, passes or other pictures that don't actively support the text. If you can make an illustration that really fits the context, fine, otherwise better leave it without. Thank you

Target Market(s)

Expats living in Switzerland. High income earners / high net worth individuals

Industry/Entity Type

tax/accounting

Number of Pages Required

1 page

Font styles to use
Other font styles liked:
• Montserrat

Colors
0054AA
0677BA
7BADD7
CADEEF
E8F1F8

Requirements
Must have
• based on general website design
Nice to have
• intuitive, flowy, attractive representation of much text
Should not have
• basic copy/paste of the text in sections :)

```html
<!DOCTYPE html>
<html lang="en">
<head>
<meta charset="utf-8">
<title>Living and working in Switzerland – Fiscaverde Advisory</title>
<link rel="stylesheet" href="https://fonts.googleapis.com/css2?family=Montserrat:wght@300;400;500;600&display=swap">
<style>
  :root {
    --white: #ffffff;
    --navy: #1f3448;
    --navy-deep: #0a2b46;
    --greenblue: #1c3a5a;
    --band: #dfe6ee;
    --mist: #eef2f6;
    --muted: #b5bfc8;
    --slate: #8595a4;
    --body: #6b7785;
    --topic: #5b7b9b;
    --accent: #3f74ad;
    --rule: #dde3e9;
    --accent-rule: #b5c9dd;
  }
  * { box-sizing: border-box; margin: 0; padding: 0; }
  html, body { width: 1200px; height: 3031px; overflow: hidden; }
  body { font-family: "Montserrat", Arial, sans-serif; background: var(--mist); color: var(--body); }
  .page { position: relative; width: 1200px; height: 3031px; overflow: hidden; background: var(--mist); }

  /* header */
  .site-header { position: absolute; top: 0; left: 0; width: 1200px; height: 65px; background: linear-gradient(90deg, #fff 0%, #f3f6f9 60%, #fff 100%); z-index: 5; }
  .brand { position: absolute; left: 129px; top: 14px; display: flex; align-items: center; gap: 10px; }
  .brand-mark { width: 38px; height: 38px; border-radius: 50%; border: 3px solid var(--navy); }
  .brand-name { font-size: 17px; font-weight: 500; color: var(--navy); line-height: 1.05; letter-spacing: .5px; text-transform: uppercase; }
  .main-nav { position: absolute; top: 27px; left: 0; font-size: 12px; color: #3c5670; }
  .main-nav a { position: absolute; white-space: nowrap; text-decoration: none; color: inherit; }
  .main-nav a.current { color: var(--navy); font-weight: 600; }
  .caret { display: inline-block; border-left: 3.5px solid transparent; border-right: 3.5px solid transparent; border-top: 4px solid #3c5670; margin-left: 3px; vertical-align: middle; }
  .btn-calc { position: absolute; left: 965px; top: 20px; width: 102px; height: 31px; background: var(--greenblue); color: #fff; font-size: 12.5px; display: flex; align-items: center; gap: 9px; padding-left: 9px; }

  /* hero */
  .hero { position: absolute; top: 65px; left: 0; width: 1200px; height: 327px; background: linear-gradient(180deg, #72869b 0%, #5b7088 55%, #4b6178 100%); }
  .hero-tower { position: absolute; left: 716px; top: 20px; width: 156px; height: 307px; background: linear-gradient(180deg, #3b4f63, #2f4357); opacity: .85; }
  .hero-eyebrow { position: absolute; left: 157px; top: 172px; font-size: 13px; color: #fff; letter-spacing: .2px; }
  .hero-title { position: absolute; left: 157px; top: 197px; font-size: 45px; line-height: 48px; color: #fff; font-weight: 400; }
  .hero-title span { display: block; font-weight: 300; }
  .menu-toggle { position: absolute; left: 820px; top: 221px; width: 49px; height: 51px; border: 1px solid #fff; border-radius: 6px; display: flex; flex-direction: column; justify-content: center; align-items: center; gap: 4px; }
  .menu-toggle i { display: block; width: 17px; height: 1.6px; background: #fff; }

  /* dark sections */
  .band-dark { position: absolute; left: 0; width: 1200px; background: var(--navy); }
  .band-one { top: 388px; height: 445px; }
  .band-two { top: 2011px; height: 1020px; }
  .chapter-no { position: absolute; left: 0; width: 1200px; text-align: center; font-weight: 300; color: #2d4660; }
  .chapter-title { position: absolute; left: 0; width: 1200px; text-align: center; color: #fff; font-weight: 400; font-size: 35px; line-height: 38px; }
  .chapter-intro { position: absolute; text-align: center; color: var(--muted); font-size: 12px; line-height: 19px; font-weight: 300; }

  /* cards */
  .card { position: absolute; background: #fff; }
  .card-head { height: 59px; background: var(--band); display: flex; align-items: center; justify-content: space-between; }
  .card-title { font-size: 22px; font-weight: 400; color: #5e7387; }
  .card-tag { font-size: 12.5px; color: var(--slate); }
  .topic-title { position: relative; font-size: 18px; font-weight: 400; color: var(--topic); padding-bottom: 17px; border-bottom: 1px solid var(--rule); margin-right: -62px; }
  .topic-title.marked::after { content: ""; position: absolute; left: 0; bottom: -2px; width: 101px; height: 3px; background: var(--accent-rule); }
  .copy p { font-size: 12.5px; line-height: 20px; font-weight: 300; color: var(--body); margin-bottom: 12px; }
  .copy ul { list-style: none; }
  .copy li { font-size: 12.5px; line-height: 20px; font-weight: 300; margin-bottom: 12px; padding-left: 26px; position: relative; }
  .copy li::before { content: "•"; position: absolute; left: 0; font-size: 10px; }
  .fold { height: 60px; display: flex; align-items: center; justify-content: space-between; border-bottom: 1px solid var(--rule); font-size: 17.5px; color: #5e7892; padding-right: 6px; }
  .fold:last-child { border-bottom: 0; }
  .fold .plus { font-size: 17px; color: var(--slate); font-weight: 300; }
  .story h3 { font-size: 19px; font-weight: 400; color: var(--accent); margin-bottom: 32px; }
  .story p { font-size: 12.5px; line-height: 20px; font-weight: 300; color: var(--body); margin-bottom: 12px; }
</style>
</head>
<body>
<div class="page">

  <header class="site-header">
    <div class="brand"><span class="brand-mark"></span><span class="brand-name">Fiscaverde<br>Advisory</span></div>
    <nav class="main-nav">
      <a class="current" style="left:449px">Home</a>
      <a style="left:508px">Tax returns</a>
      <a style="left:595px">More services<span class="caret"></span></a>
      <a style="left:706px">Swiss tax guide</a>
      <a style="left:818px">About us</a>
    </nav>
    <div class="btn-calc">
      <svg width="12" height="15" viewBox="0 0 12 15"><rect x="0.5" y="0.5" width="11" height="14" fill="none" stroke="#fff"/><rect x="2.5" y="2.5" width="7" height="3" fill="#fff"/><g fill="#fff"><rect x="2.5" y="7.5" width="2" height="2"/><rect x="7.5" y="7.5" width="2" height="2"/><rect x="2.5" y="11" width="2" height="2"/><rect x="7.5" y="11" width="2" height="2"/></g></svg>
      Calculate
    </div>
  </header>

  <section class="hero">
    <div class="hero-tower" role="img" aria-label="Hazy city skyline with a tall glass office tower"></div>
    <p class="hero-eyebrow">RESOURCES</p>
    <h1 class="hero-title">Living and working<span>in Switzerland</span></h1>
    <div class="menu-toggle"><i></i><i></i><i></i></div>
  </section>

  <section class="band-dark band-one">
    <div class="chapter-no" style="top:70px;font-size:96px;line-height:96px;">1</div>
    <h2 class="chapter-title" style="top:110px;">Life in Switzerland</h2>
    <p class="chapter-intro" style="left:350px;width:500px;top:200px;">To give &nbsp;you a small impression of what to expect when living in Switzerland, we have put together some topics for you to make your new start in Switzerland as pleasant as possible.</p>
  </section>

  <svg style="position:absolute;left:0;top:370px" width="1200" height="480" viewBox="0 370 1200 480">
    <polygon points="0,376 716,390 0,401" fill="#d5dde5"/>
    <polygon points="0,836 245,830 245,833 0,848" fill="#d5dde5"/>
  </svg>

  <article class="card" style="left:245px;top:686px;width:720px;height:920px;">
    <div class="card-head" style="padding:0 26px 0 29px;">
      <h3 class="card-title">General</h3><span class="card-tag">Life in Switzerland</span>
    </div>
    <div class="copy" style="padding:41px 62px 0 57px;">
      <h4 class="topic-title">4 official languages</h4>
      <div style="margin-top:30px;">
        <p>Unlike many other countries in Europe, where there is usually only one official national language, Switzerland has four of them: German, French, Italian and Romansh.</p>
        <p>The most widespread language is German, which is spoken mainly in central Switzerland and the cantons bordering Germany.</p>
        <p>French dominates in the western part of Switzerland, and Italian in the southeastern part.</p>
        <p>Rhaeto-Romanic is spoken by only a very small part of the total population in eastern Switzerland.</p>
        <p>In each region, there are also different dialects in the various languages.</p>
      </div>
      <h4 class="topic-title marked" style="margin-top:34px;">Currency and banking</h4>
      <div style="margin-top:28px;">
        <p>The national currency in Switzerland is the Swiss franc (CHF). 1 Swiss franc (Franken) is equal to 100 centimes (Rappen).</p>
        <p>The banknotes are available in the following amounts: 10, 20, 50, 100, 200, 1000.</p>
        <p>For coins, there are the following denominations:</p>
        <ul><li>CHF 1, 2, 5</li><li>5, 10, 20, 50 centimes</li></ul>
        <p>Current accounts can be opened at any major bank, Swiss postal bank, cantonal or private banks. The largest banks in Switzerland are: Alpenhorn Bank, Helvia Bank and PostVerde.</p>
      </div>
      <div style="margin:8px -8px 0 -3px;">
        <div class="fold">Public holidays<span class="plus">+</span></div>
        <div class="fold">Usual business and store opening hours<span class="plus">+</span></div>
        <div class="fold">Electricity and water<span class="plus">+</span></div>
        <div class="fold">Telephone and television<span class="plus">+</span></div>
      </div>
    </div>
  </article>

  <article class="card" style="left:245px;top:1654px;width:720px;height:289px;">
    <div class="card-head" style="height:56px;padding-left:20px;">
      <h3 class="card-title">Living in Switzerland</h3>
    </div>
    <div class="copy" style="padding:28px 62px 0 52px;">
      <p>The Swiss housing and real estate market varies greatly from region to region in terms of purchase and rental prices. In highly sought-after areas or larger cities, prices are relatively high, while living in rural areas is less expensive.</p>
      <div style="margin-top:8px;">
        <div class="fold" style="height:51px;padding-top:8px;">Rent<span class="plus">+</span></div>
        <div class="fold" style="height:50px;">Buy<span class="plus">+</span></div>
      </div>
    </div>
  </article>

  <section class="band-dark band-two">
    <div class="chapter-no" style="top:55px;left:14px;font-size:150px;line-height:150px;color:#223f63;">2</div>
    <h2 class="chapter-title" style="top:102px;">Switzerland - a brief overview of<br>the Alpine country</h2>
    <p class="chapter-intro" style="left:300px;width:614px;top:245px;">Every year, Switzerland attracts many new citizens who want to settle there temporarily or long-term, and not without reason, because life in Switzerland is characterized by a high quality. If you are also thinking of settling here, we would like to introduce you to the country in the following.</p>
  </section>

  <svg style="position:absolute;left:0;top:2400px" width="1200" height="631" viewBox="0 2400 1200 631">
    <polygon points="0,2493 1200,2417 1200,3031 0,3031" fill="#eef2f6"/>
  </svg>

  <article class="card story" style="left:260px;top:2365px;width:691px;height:666px;padding:63px 43px 0 53px;">
    <h3>A strong federation</h3>
    <p>Switzerland is divided into 26 cantons, which have partial sovereignty and a capital. Together, the cantons form the Swiss Confederation - the federal state. The capital of the federal state is Bern. Unlike many other countries around the world, the political system in Switzerland is a direct democracy. The resulting autonomy as well as the willingness to compromise are deeply rooted in Swiss culture. Furthermore, neutrality in foreign policy issues is part of the self-image of Swiss</p>
    <h3 style="margin-top:24px;">A diverse population structure</h3>
    <p>Many ethnicities and cultures meet in Switzerland. Of the total population of 8.6 million, one in four is a foreigner. Italians, Germans and Portuguese make up the largest proportion of expatriate Swiss. However, the number of non-European immigrants is growing steadily.</p>
    <p>There are four official languages in Switzerland: German, French, Italian and Romansh. This alone shows that cultural identity here is based less on a common language or ethnic origin than on intercultural exchange.</p>
    <h3 style="margin-top:28px;">Excellent economy</h3>
    <p>Switzerland is one of the richest countries in the world. It has its solid economy to thank for that. The gross domestic product per capita is the equivalent of almost 82,000 US dollars (as of 2019). This puts Switzerland in second place, beaten only by Luxembourg in this category. The driving economic forces in Switzerland are the service sector, pharmaceuticals and watchmaking.</p>
    <h3 style="margin-top:28px;">High standard of living</h3>
    <p>The robust economy enables people in Switzerland to enjoy a high standard of living. It is not for nothing that Swiss cities rank among the best places to live.</p>
  </article>

</div>
</body>
</html>
```